Restaurant Posters

Looking for two posters to be created for restaurant promos - see below for details:

Design #1 -
Want to highlight two main specials we offer - first is Tuesday BOGO Burgers (with purchase of two beverages), second is on Wednesday's we offer $0.75 Wings (includes traditional and boneless) and $2 off IPA's

Then at the bottom smaller would like to call out two less important offers - first is $2 off Nebraska Beers on Mondays, and the second is 1/2 off 19.2oz Crowlers on Thursdays

Design #2 -
Looking to create a sign up for our e-club and receive a free appetizer upon sign up, free burger on your birthday week, and access to exclusive deals and email offers

See attached for supporting docs you may use - don't have to but feel free to get creative with these. Would like the designs to be simple, and follow our brand look and feel as much as possible. Our website is not a good indication of our brand - I would go more off of our logos, and our menu design.

Need extra days to review

```html
<!DOCTYPE html>
<html lang="en">
<head>
<meta charset="utf-8">
<title>Prairie Tap House – Daily Specials</title>
<link rel="stylesheet" href="https://fonts.googleapis.com/css2?family=Bebas+Neue&family=Montserrat:wght@900&family=Oswald:wght@400;600&family=Roboto+Slab:wght@400;500&display=swap">
<style>
  :root {
    --page-bg: #f6f6f6;
    --brand-red: #d8223a;
    --brand-red-deep: #c81d33;
    --card-white: #ffffff;
    --ink: #111111;
    --dash: #222222;
  }
  * { box-sizing: border-box; margin: 0; padding: 0; }
  html, body {
    width: 1200px; height: 1200px; overflow: hidden;
    background: var(--page-bg);
  }
  .poster {
    position: absolute; left: 191px; top: 22px;
    width: 794px; height: 1122px;
    transform: scale(1.03); transform-origin: top left;
    background: linear-gradient(180deg, var(--brand-red) 0%, var(--brand-red-deep) 100%);
  }
  .poster-title {
    position: absolute; left: 43px; top: 38px;
    font-family: "Bebas Neue", sans-serif;
    font-size: 50px; line-height: 1; letter-spacing: 0.01em;
    color: var(--card-white);
  }
  .special {
    position: absolute; background: var(--card-white); overflow: hidden;
  }
  .special::before {
    content: ""; position: absolute; inset: 10px;
    border: 1.5px dashed var(--dash);
  }
  .special--tuesday   { left: 30px;  top: 108px; width: 735px; height: 323px; }
  .special--wednesday { left: 30px;  top: 454px; width: 735px; height: 304px; }
  .special--monday    { left: 30px;  top: 784px; width: 356px; height: 298px; }
  .special--thursday  { left: 408px; top: 784px; width: 357px; height: 298px; }

  .day {
    position: absolute;
    font-family: "Bebas Neue", sans-serif;
    font-size: 42px; line-height: 1; color: var(--ink);
    letter-spacing: 0.01em;
  }
  .offer {
    position: absolute; z-index: 2;
    font-family: "Montserrat", sans-serif; font-weight: 900;
    color: var(--ink); letter-spacing: 0.12em; line-height: 1;
    text-transform: uppercase; white-space: nowrap;
  }
  .offer--hero { font-size: 44px; line-height: 1.08; }
  .offer--mid { font-size: 27px; }
  .offer--small { font-size: 22px; line-height: 1.25; }
  .note {
    position: absolute;
    font-family: "Roboto Slab", serif; font-weight: 500; font-size: 15px; line-height: 1.35;
    color: var(--ink);
  }
  .timing {
    position: absolute;
    font-family: "Oswald", sans-serif; font-size: 16px; color: var(--ink);
    transform: scaleX(0.88); transform-origin: left center;
  }
  .timing strong { font-weight: 600; margin-left: 6px; }
  .visual { position: absolute; border-radius: 14px; }
  .visual--burger {
    left: 336px; top: 62px; width: 222px; height: 230px; border-radius: 50% 50% 30% 30%;
    background: radial-gradient(circle at 50% 35%, #f2b36b 0%, #d9783a 45%, #8a4a26 100%);
  }
  .visual--cans {
    left: 494px; top: 30px; width: 190px; height: 256px; border-radius: 16px;
    background: linear-gradient(90deg, #b9bcc0 0%, #f1f2f3 40%, #c9cbce 70%, #9ea1a5 100%);
  }
  .visual--glass {
    left: 311px; top: 40px; width: 116px; height: 235px; border-radius: 12px;
    background: linear-gradient(180deg, #f4f1e6 0%, #f6cf5a 15%, #eba52c 100%);
  }
  .visual--bites {
    left: 282px; top: 180px; width: 288px; height: 96px; border-radius: 40px;
    background: radial-gradient(ellipse at 55% 45%, #e59a45 0%, #c8651f 60%, #9a4a1a 100%);
  }
  .visual--glass-small {
    left: 231px; top: 72px; width: 72px; height: 200px; border-radius: 10px;
    background: linear-gradient(180deg, #f4f1e6 0%, #f6cf5a 22%, #eba52c 100%);
  }
  .visual--can-pour {
    left: 226px; top: 20px; width: 104px; height: 260px; border-radius: 14px;
    background: linear-gradient(200deg, #f0b33a 0%, #e8e9ea 35%, #b7babe 100%);
  }
</style>
</head>
<body>
  <main class="poster">
    <h1 class="poster-title">DAILY SPECIALS</h1>

    <section class="special special--tuesday">
      <h2 class="day" style="left:45px; top:40px;">TUESDAYS:</h2>
      <p class="offer offer--hero" style="left:45px; top:88px;">BOGO<br>BURGERS</p>
      <p class="note" style="left:46px; top:194px;">With purchase of 2 beverages.</p>
      <p class="timing" style="left:46px; top:224px;">Timings:<strong>4pm onwards</strong></p>
      <div class="visual visual--cans" role="img" aria-label="Two silver craft beer cans"></div>
      <div class="visual visual--burger" role="img" aria-label="Loaded burger with crispy toppings and sauce"></div>
    </section>

    <section class="special special--wednesday">
      <h2 class="day" style="left:35px; top:44px;">WEDNESDAYS:</h2>
      <p class="offer offer--mid" style="left:35px; top:99px;">$0.75 WINGS</p>
      <p class="note" style="left:35px; top:140px;">Your choice of Bone-in<br>or Boneless wings.</p>
      <p class="timing" style="left:35px; top:196px;">Timings:<strong>All Day</strong></p>
      <div class="visual visual--glass" role="img" aria-label="Pint glass of golden IPA"></div>
      <div class="visual visual--bites" role="img" aria-label="Crispy fried bites"></div>
      <p class="offer offer--mid" style="left:467px; top:99px; line-height:1.25;">AND $2 OFF<br>IPA PINTS</p>
    </section>

    <section class="special special--monday">
      <h2 class="day" style="left:34px; top:36px;">MONDAYS:</h2>
      <p class="offer offer--small" style="left:34px; top:86px;">$2 OFF<br>NEBRASKA<br>BREWED<br>BEERS<br>ON TAP</p>
      <p class="timing" style="left:35px; top:240px;">Timings:<strong>All Day</strong></p>
      <div class="visual visual--glass-small" role="img" aria-label="Glass of golden beer with foam splash"></div>
    </section>

    <section class="special special--thursday">
      <h2 class="day" style="left:32px; top:36px;">THURSDAYS:</h2>
      <p class="offer offer--small" style="left:32px; top:92px; line-height:1.3; letter-spacing:0.11em;">½ OFF<br>19.2 OZ<br>CROWLERS</p>
      <p class="timing" style="left:30px; top:228px;">Timings:<strong>All Day</strong></p>
      <div class="visual visual--can-pour" role="img" aria-label="Silver crowler can with beer splashing out"></div>
    </section>
  </main>
</body>
</html>
```